Visitenkarten für Elektro- und Informationstechnik-Betrieb
Zielgruppe
Wir sind ein Elektro- und Informationstechnik-Betrieb.
Unsere Fachgebiete sind Photovoltaikanlagen, Stromspeicher, Smart-Home und Ladestationrn
Aufgabenstellung
Design in der Farben des Logos und ein dunkler Hintergrund.

```html
<!DOCTYPE html>
<html lang="de">
<head>
<meta charset="utf-8">
<title>Visitenkarten – Elektro- und Informationstechnik Falkner</title>
<link href="https://fonts.googleapis.com/css2?family=Arimo:wght@400;700&display=swap" rel="stylesheet">
<style>
  :root {
    --page: #d9d7d3;
    --card: #050505;
    --blue: #5e8fb3;
    --orange: #d7783a;
    --text-font: "Arimo", Arial, sans-serif;
  }
  * { box-sizing: border-box; margin: 0; padding: 0; }
  html, body { width: 1200px; height: 873px; overflow: hidden; }
  body {
    background: var(--page);
    font-family: var(--text-font);
    display: flex;
    align-items: center;
    justify-content: center;
    gap: 44px;
  }
  .card {
    position: relative;
    width: 520px;
    height: 336px;
    background: var(--card);
    box-shadow: 0 10px 24px rgba(0,0,0,.28);
    overflow: hidden;
  }
  .card-front .accent-band {
    position: absolute; left: 0; right: 0; bottom: 0;
    height: 9px; background: var(--orange);
  }
  .contact-person { position: absolute; left: 34px; top: 34px; }
  .person-name {
    color: var(--blue); font-weight: 700; font-size: 21px; letter-spacing: .3px;
  }
  .person-role {
    color: var(--orange); font-size: 13px; margin-top: 3px;
  }
  .address {
    position: absolute; left: 34px; top: 104px;
    color: var(--blue); font-size: 15px; line-height: 23px;
  }
  .address-line { position: relative; }
  .address-line svg { position: absolute; left: -15px; top: 5px; }
  .brand {
    position: absolute; right: 40px; top: 150px;
    display: flex; align-items: center; gap: 10px;
  }
  .brand-dot { width: 10px; height: 10px; border-radius: 50%; background: var(--orange); }
  .brand-name {
    color: var(--blue); font-weight: 400; font-size: 28px;
  }
  .contact-list {
    position: absolute; right: 30px; bottom: 28px;
    list-style: none; color: var(--blue); font-size: 15px; line-height: 25px;
  }
  .contact-list li { display: flex; align-items: center; gap: 9px; }
  .contact-list svg { flex: none; }
  .card-back .brand {
    right: auto; top: 50%; left: 50%; transform: translate(-50%, -50%);
  }
  .card-back .brand-name { font-size: 34px; }
</style>
</head>
<body>
  <section class="card card-front" aria-label="Vorderseite">
    <div class="contact-person">
      <p class="person-name">LARS FALKNER</p>
      <p class="person-role">Ansprechpartner</p>
    </div>
    <div class="address">
      <p class="address-line">
        <svg width="10" height="13" viewBox="0 0 10 13"><path d="M5 0a4.5 4.5 0 0 0-4.5 4.5C.5 8 5 13 5 13s4.5-5 4.5-8.5A4.5 4.5 0 0 0 5 0zm0 6.3a1.8 1.8 0 1 1 0-3.6 1.8 1.8 0 0 1 0 3.6z" fill="var(--orange)"/></svg>
        Elektro- und Informationstechnik Falkner
      </p>
      <p>Am Lindenhang 7</p>
      <p>66540 Eichweiler</p>
    </div>
    <div class="brand">
      <span class="brand-dot"></span>
      <span class="brand-name">Falkner</span>
    </div>
    <ul class="contact-list">
      <li>
        <svg width="12" height="12" viewBox="0 0 12 12"><path d="M2.5 .5l2 2.5-1 1.3a7 7 0 0 0 4.2 4.2l1.3-1 2.5 2-1.3 1.8C5.5 11 1 6.5.7 1.8z" fill="var(--orange)"/></svg>
        +49 157 30418265
      </li>
      <li>
        <svg width="13" height="10" viewBox="0 0 13 10"><rect x=".5" y=".5" width="12" height="9" fill="var(--orange)"/><path d="M.5 .5l6 5 6-5" stroke="var(--card)" fill="none"/></svg>
        service@elektro-it-falkner.de
      </li>
      <li>
        <svg width="12" height="12" viewBox="0 0 12 12"><circle cx="6" cy="6" r="5.5" fill="var(--orange)"/><path d="M.5 6h11M6 .5v11M2 3h8M2 9h8" stroke="var(--card)" stroke-width=".8"/></svg>
        www.elektro-it-falkner.de
      </li>
    </ul>
    <div class="accent-band"></div>
  </section>

  <section class="card card-back" aria-label="Rückseite">
    <div class="brand">
      <span class="brand-dot"></span>
      <span class="brand-name">Falkner</span>
    </div>
  </section>
</body>
</html>
```